Tallbridge needs a new rocket based website

We need a new website that will be based on our rocket ship logo. We develop innovative solutions for enterprises. We would like to see a design that when the pages scroll, the rocket launches and goes from launch through a journey, similar to how we approach our customer. We would like areas for "Who are we", "What can we do", "What have we done", "How can we help". http://www.tallbridge.com.au is our current website

Target Market(s)

Government, Enterprise, Cloud

Industry/Entity Type

Software Service

Coding

Coded - Design and coding required

Number of Pages Required

2 page

Requirements
Must have
• We would like to see a design that when the pages scroll, the rocket launches and goes from launch through a journey, similar to how we approach our customer.
• Must have a home page and a detail page.
• Would like to see the logo/rocket animate in some way when you scroll through he page.

```html
<!DOCTYPE html>
<html lang="en">
<head>
<meta charset="utf-8">
<title>Tallbridge – Best Solutions for Your Business</title>
<link href="https://fonts.googleapis.com/css2?family=Titillium+Web:wght@400;600;700&family=Open+Sans:ital,wght@0,400;0,600;0,700;1,400&display=swap" rel="stylesheet">
<style>
:root{
  --orange:#f7941d;
  --orange-light:#fbb45a;
  --dark:#151515;
  --dark-2:#232323;
  --grey-bg:#f4f4f4;
  --text:#222;
  --muted:#777;
  --white:#fff;
}
*{box-sizing:border-box;margin:0;padding:0}
html,body{width:1200px;height:4592px;overflow:hidden}
body{font-family:"Open Sans",sans-serif;color:var(--text);background:var(--white);font-size:13px;line-height:1.55}
h1,h2,h3,h4,.brand{font-family:"Titillium Web",sans-serif}
.wrap{width:660px;margin-left:270px}
.btn{display:inline-block;background:var(--orange);color:var(--white);font-weight:700;font-size:11px;padding:9px 22px;text-transform:uppercase;letter-spacing:.5px}
.btn-outline{background:transparent;border:1px solid var(--orange)}

/* nav */
.site-nav{height:90px;display:flex;align-items:center;justify-content:space-between;padding:0 100px 0 110px;background:var(--white)}
.brand{display:flex;align-items:center;gap:8px;font-size:30px;font-weight:600;color:var(--orange);line-height:1}
.brand-mark{width:14px;height:14px;background:var(--orange)}
.nav-links{display:flex;align-items:center;gap:34px;font-size:13px;color:var(--text)}

/* hero */
.hero{height:560px;position:relative;background:linear-gradient(120deg,#2a2a2a,#0e0e0e 55%,#3a3128);color:var(--white);text-align:center}
.hero-inner{position:absolute;top:190px;left:0;right:0}
.hero h1{font-size:52px;line-height:1.05;font-weight:700;text-transform:uppercase}
.hero p{font-size:24px;margin:24px auto 30px;width:300px;line-height:1.4}

/* who + rocket journey */
.who{height:560px;background:var(--grey-bg);padding-top:110px;position:relative}
.rocket{position:absolute;left:100px;top:-10px;width:70px;height:320px;border-radius:35px 35px 6px 6px;background:linear-gradient(180deg,var(--orange-light),var(--orange) 55%,#e07d0a)}
.who .wrap{display:flex;gap:50px}
.who-text{width:430px}
.section-title{font-size:28px;font-weight:700;text-transform:uppercase;margin-bottom:16px}
.who-lead{color:var(--orange);font-weight:700;font-size:14px;text-transform:uppercase;margin-bottom:14px;line-height:1.4}
.who-photo{width:215px;height:160px;margin-top:70px;background:linear-gradient(135deg,#8a8076,#4c4640);border-top:4px solid var(--orange);border-right:4px solid var(--orange)}

/* can do */
.can-do{height:540px;background:linear-gradient(100deg,#121212,#2b2b2b 60%,#1a1a1a);color:var(--white);padding-top:92px}
.can-do .intro{font-weight:700;font-size:14px;margin-bottom:60px}
.services{display:flex;gap:12px;width:800px}
.service{width:185px;padding:14px;height:150px}
.service.active{border:1px solid #bbb}
.service-icon{width:34px;height:34px;margin-bottom:20px}
.service h4{font-size:15px;font-weight:700;margin-bottom:8px}
.service p{font-size:10px;font-weight:600}

/* done */
.done{height:760px;background:var(--grey-bg);padding-top:92px;position:relative}
.cards{display:flex;gap:50px;margin-top:38px;width:1000px}
.card{width:275px}
.card.faded{opacity:.4}
.card-photo{height:180px;position:relative}
.card-photo::after{content:"";position:absolute;top:-10px;right:-10px;width:80px;height:60px;border-top:8px solid var(--orange);border-right:8px solid var(--orange)}
.card-head{display:flex;gap:12px;align-items:flex-start;margin-top:-34px;position:relative}
.date-badge{background:var(--orange);color:var(--white);width:60px;padding:6px 8px;font-family:"Titillium Web",sans-serif;font-weight:700;line-height:1}
.date-badge b{font-size:22px;display:block}
.date-badge span{font-size:10px}
.card-meta{padding-top:38px}
.card-meta small{font-size:10px;color:var(--muted);display:block;line-height:1.2}
.card h3{font-size:22px;line-height:1.1}
.card p{font-size:11px;margin:10px 0 22px 72px;width:200px}
.card .btn{margin-left:72px;padding:6px 16px;font-size:10px}
.arrows{display:flex;gap:16px;margin-top:60px}

/* help */
.help{height:700px;background:var(--orange);position:relative;color:var(--white)}
.help-circle{position:absolute;left:120px;top:250px;width:360px;height:360px;border-radius:50%;background:#f6a544}
.help-portrait{position:absolute;left:150px;top:135px;width:280px;height:480px;background:linear-gradient(180deg,#b9b9b9,#555 60%,#3c3c3c);border-radius:120px 120px 0 0}
.help-content{position:absolute;left:600px;top:80px;width:480px}
.help-title{font-size:30px;margin-bottom:40px}
.step{display:flex;gap:24px;margin-bottom:40px}
.step-num{flex:none;width:36px;height:36px;border-radius:50%;background:var(--white);color:var(--orange);font-weight:700;font-size:20px;display:flex;align-items:center;justify-content:center;font-family:"Titillium Web",sans-serif}
.step h4{font-size:20px;text-transform:uppercase}
.step p{font-size:12px;font-weight:600;color:#fff3e3}

/* testimonials */
.testimonials{height:580px;background:var(--white);padding-top:56px}
.testimonials .section-title{margin-left:240px}
.quotes{display:flex;gap:60px;margin-left:250px;margin-top:20px}
.quote{width:300px}
.quote.faded{opacity:.4}
.quote-box{background:var(--white);box-shadow:0 2px 14px rgba(0,0,0,.12);padding:26px 32px 40px;font-style:italic;font-size:12px;text-align:center;position:relative;min-height:140px}
.quote-mark{position:absolute;right:30px;bottom:0;color:var(--orange);font-size:34px;font-weight:700;font-style:normal;line-height:1}
.author{display:flex;align-items:center;justify-content:center;gap:12px;margin-top:22px}
.author-name{text-align:right;font-size:11px}
.author-name b{color:var(--orange);display:block;font-size:13px}
.avatar{width:56px;height:56px;border-radius:50%;background:linear-gradient(135deg,#999,#555)}
.testimonials .arrows{margin-left:285px;margin-top:50px}

/* contact */
.contact{height:400px;background:linear-gradient(100deg,#1a1a1a,#0d0d0d);color:var(--white);padding-top:50px}
.contact h2{text-align:center;font-size:36px;margin-bottom:50px}
.form{width:720px;margin-left:232px}
.form-row{display:flex;gap:50px;margin-bottom:40px}
.field{flex:1;border-bottom:1px solid #777;padding-bottom:8px;font-weight:700;font-size:13px}
.form-foot{display:flex;align-items:center;justify-content:space-between;margin-top:-10px}
.check{display:flex;align-items:center;gap:8px;font-size:11px}
.check i{width:16px;height:16px;background:var(--white)}
.send{display:flex;align-items:center;gap:14px;font-size:10px;font-weight:700;text-align:right}

/* footer */
.site-footer{height:402px;background:var(--dark);color:var(--white);padding:60px 0 0 140px;display:flex;align-items:flex-start;gap:150px}
.site-footer .brand{font-size:26px;margin-top:4px}
.footer-cols{display:flex;gap:70px}
.footer-cols h4{font-size:15px;margin-bottom:6px}
.footer-cols li{list-style:none;font-size:11px;font-weight:600;line-height:1.5}
</style>
</head>
<body>

<header class="site-nav">
  <div class="brand"><span class="brand-mark"></span>Tallbridge</div>
  <nav class="nav-links">
    <span>Who are we</span><span>What can we do</span><span>What have we done</span><span>How we can help you</span>
    <span class="btn">Get in touch</span>
  </nav>
</header>

<section class="hero" role="img" aria-label="Background photo: business people shaking hands in a dark office">
  <div class="hero-inner">
    <h1>Best solutions for<br>your business</h1>
    <p>Tallbridge, Innovative software solutions</p>
    <span class="btn btn-outline">Get in touch</span>
  </div>
</section>

<section class="who">
  <div class="rocket" role="img" aria-label="Illustration: orange rocket with flame trail that launches and travels down the page on scroll"></div>
  <div class="wrap">
    <div class="who-text">
      <h2 class="section-title">Who are we?</h2>
      <p class="who-lead">Lorem ipsum dolor sit amet, consectetuer aenean commodo ligula eget dolor.</p>
      <p>Lorem ipsum dolor sit amet, consectetuer adipiscing elit. Aenean commodo ligula eget dolor. Aenean massa. Cum sociis natoque penatibus et magnis dis parturient montes, nascetur ridiculus mus. Donec quam felis, ultricies nec, pellentesque eu, pretium quis, sem. Nulla consequat massa quis enim. Donec pede justo, fringilla vel, aliquet nec, vulputate eget, arcu. In enim justo, rhoncus ut, imperdiet a, venenatis vitae, justo.</p>
    </div>
    <div class="who-photo" role="img" aria-label="Photo: team working together around a meeting table"></div>
  </div>
</section>

<section class="can-do" role="img" aria-label="Background photo: hands typing on a laptop keyboard">
  <div class="wrap">
    <h2 class="section-title">What can we do?</h2>
    <p class="intro">Lorem ipsum dolor sit amet, consectetuer adipiscing elit. Aenean commodo ligula eget dolor. Aenean massa. Cum sociis natoque penatibus et magnis dis parturient montes, nascetur ridiculus mus.</p>
    <div class="services">
      <div class="service">
        <svg class="service-icon" viewBox="0 0 34 34" fill="none" stroke="#f7941d" stroke-width="2"><rect x="4" y="6" width="26" height="22"/><line x1="4" y1="13" x2="30" y2="13"/><line x1="10" y1="19" x2="24" y2="19"/></svg>
        <h4>e-Fulfilment</h4><p>All of your Parliamentary software and business process needs.</p>
      </div>
      <div class="service">
        <svg class="service-icon" viewBox="0 0 34 34" fill="none" stroke="#f7941d" stroke-width="2"><rect x="4" y="6" width="26" height="22"/><line x1="4" y1="13" x2="30" y2="13"/><line x1="10" y1="19" x2="24" y2="19"/></svg>
        <h4>Cloud</h4><p>All of your Parliamentary software and business process needs.</p>
      </div>
      <div class="service">
        <svg class="service-icon" viewBox="0 0 34 34" fill="none" stroke="#f7941d" stroke-width="2"><rect x="4" y="6" width="26" height="22"/><line x1="4" y1="13" x2="30" y2="13"/><line x1="10" y1="19" x2="24" y2="19"/></svg>
        <h4>Architecture and design</h4><p>All of your Parliamentary software and business process needs.</p>
      </div>
      <div class="service active">
        <svg class="service-icon" viewBox="0 0 34 34" fill="none" stroke="#f7941d" stroke-width="2"><rect x="4" y="6" width="26" height="22"/><line x1="4" y1="13" x2="30" y2="13"/><line x1="10" y1="19" x2="24" y2="19"/></svg>
        <h4>Software development</h4><p>All of your Parliamentary software and business process needs.</p>
      </div>
    </div>
  </div>
</section>

<section class="done">
  <div class="wrap">
    <h2 class="section-title">What have we done?</h2>
    <div class="cards">
      <article class="card">
        <div class="card-photo" role="img" aria-label="Photo: business meeting with laptops" style="background:linear-gradient(135deg,#9a8f86,#4a4540)"></div>
        <div class="card-head"><div class="date-badge"><b>SEP</b><span>01, 2018</span></div><div class="card-meta"><small>2018-03-17</small><h3>Work Headline</h3></div></div>
        <p>Lorem ipsum dolor sit amet lorem ipsum commodo ligula commodo aenean et in volutpat amet sodales porttitor bibendum facilisi imperdiet aliquam ipsum ante morbi sed ipsum mollis a.</p>
        <span class="btn">Read more</span>
      </article>
      <article class="card">
        <div class="card-photo" role="img" aria-label="Photo: smiling businessman at a desk" style="background:linear-gradient(135deg,#c9c2b8,#7a6d62)"></div>
        <div class="card-head"><div class="date-badge"><b>SEP</b><span>01, 2018</span></div><div class="card-meta"><small>2018-03-17</small><h3>Work Headline</h3></div></div>
        <p>Lorem ipsum dolor sit amet lorem ipsum commodo ligula commodo aenean et in volutpat amet sodales porttitor bibendum facilisi imperdiet aliquam ipsum ante morbi sed ipsum mollis a.</p>
        <span class="btn">Read more</span>
      </article>
      <article class="card faded">
        <div class="card-photo" role="img" aria-label="Photo: hands on a touch table in an office" style="background:linear-gradient(135deg,#ddd,#888)"></div>
        <div class="card-head"><div class="date-badge"><b>SEP</b><span>01, 2018</span></div><div class="card-meta"><small>2018-03-17</small><h3>Work Headline</h3></div></div>
        <p>Lorem ipsum dolor sit amet lorem ipsum commodo ligula commodo aenean et in volutpat amet sodales porttitor bibendum facilisi imperdiet aliquam ipsum ante morbi sed ipsum mollis a.</p>
        <span class="btn">Read more</span>
      </article>
    </div>
    <div class="arrows">
      <svg width="34" height="14" viewBox="0 0 34 14" fill="none" stroke="#bbb" stroke-width="2"><path d="M33 7H2M8 1 2 7l6 6"/></svg>
      <svg width="34" height="14" viewBox="0 0 34 14" fill="none" stroke="#f7941d" stroke-width="2"><path d="M1 7h31M26 1l6 6-6 6"/></svg>
    </div>
  </div>
</section>

<section class="help">
  <div class="help-circle"></div>
  <div class="help-portrait" role="img" aria-label="Photo: confident businessman in a grey suit with arms crossed"></div>
  <div class="help-content">
    <h2 class="section-title help-title">How we can help you?</h2>
    <div class="step"><span class="step-num">1</span><div><h4>Headline of the section</h4><p>Lorem ipsum dolor sit amet, consectetuer adipiscing elit. Aenean commodo ligula eget dolor. Aenean massa. Cum sociis natoque penatibus et magnis dis parturient montes, nascetur ridiculus mus. Donec quam felis.</p></div></div>
    <div class="step"><span class="step-num">2</span><div><h4>Headline of the section</h4><p>Lorem ipsum dolor sit amet, consectetuer adipiscing elit. Aenean commodo ligula eget dolor. Aenean massa. Cum sociis natoque penatibus et magnis dis parturient montes, nascetur ridiculus mus. Donec quam felis.</p></div></div>
    <div class="step"><span class="step-num">3</span><div><h4>Headline of the section</h4><p>Lorem ipsum dolor sit amet, consectetuer adipiscing elit. Aenean commodo ligula eget dolor. Aenean massa. Cum sociis natoque penatibus et magnis dis.</p></div></div>
  </div>
</section>

<section class="testimonials">
  <h2 class="section-title">Testimonials</h2>
  <div class="quotes">
    <div class="quote"><div class="quote-box">Lorem ipsum dolor sit amet, consectetuer adipiscing elit. Aenean commodo ligula eget dolor. Aenean massa. Cum sociis natoque penatibus et magnis.<span class="quote-mark">”</span></div>
      <div class="author"><div class="author-name"><b>Sam Hollis</b>Service Provider</div><div class="avatar" role="img" aria-label="Client portrait"></div></div></div>
    <div class="quote"><div class="quote-box">Lorem ipsum dolor sit amet, consectetuer adipiscing elit. Aenean commodo ligula eget dolor. Aenean massa. Cum sociis natoque penatibus et magnis.<span class="quote-mark">”</span></div>
      <div class="author"><div class="author-name"><b>Sam Hollis</b>Service Provider</div><div class="avatar" role="img" aria-label="Client portrait"></div></div></div>
    <div class="quote faded"><div class="quote-box">Lorem ipsum dolor sit amet, consectetuer adipiscing elit. Aenean commodo ligula eget dolor. Aenean massa. Cum sociis natoque penatibus et magnis.<span class="quote-mark">”</span></div>
      <div class="author"><div class="author-name"><b>Sam Hollis</b>Service Provider</div><div class="avatar" role="img" aria-label="Client portrait"></div></div></div>
  </div>
  <div class="arrows">
    <svg width="34" height="14" viewBox="0 0 34 14" fill="none" stroke="#bbb" stroke-width="2"><path d="M33 7H2M8 1 2 7l6 6"/></svg>
    <svg width="34" height="14" viewBox="0 0 34 14" fill="none" stroke="#f7941d" stroke-width="2"><path d="M1 7h31M26 1l6 6-6 6"/></svg>
  </div>
</section>

<section class="contact" role="img" aria-label="Background photo: dark office scene">
  <h2>GET IN TOUCH!</h2>
  <div class="form">
    <div class="form-row"><div class="field">Your Full Name...</div><div class="field">Your Email Address...</div></div>
    <div class="form-row"><div class="field">Write a message for us...</div></div>
    <div class="form-foot">
      <div class="check"><i></i>I'm not a robot</div>
      <div class="send"><span>We will answer<br>in 24hours</span><span class="btn">Send a message</span></div>
    </div>
  </div>
</section>

<footer class="site-footer">
  <div class="brand"><span class="brand-mark"></span>Tallbridge</div>
  <div class="footer-cols">
    <div><h4>Navigation</h4><ul><li>Who are we</li><li>What can we do</li><li>What have we done</li><li>How we can help you</li></ul></div>
    <div><h4>Policy</h4><ul><li>Conditions &amp; Terms</li><li>About us</li><li>Privacy Policy</li><li>Why Use us</li><li>Web Security</li></ul></div>
    <div><h4>Contacts</h4><ul><li>Your Email Adress</li><li>Phone Numbers</li><li>Email Addresses</li><li>Working Hours</li><li>Products</li></ul></div>
    <div><h4>Social</h4><ul><li>Network One</li><li>Network Two</li><li>Network Three</li></ul></div>
  </div>
</footer>

</body>
</html>
```